Menu Board For a Bubble Tea Trailer

Pearlwave is a bubble tea trailer that will be located in town and by the beach. Our aim is to bring refreshing beverages to our local community. My menu needs to reflect a bubbly and happy atmosphere of delicious fruit and some floral drinks, without looking unprofessional or childish.

My menu needs to be 1600mm long by 500mm high. It will be printed and attached to a sneeze guard for my beverage trailer which will be displayed on my serving window.

All drinks are priced as follows:
Regular: $6.50 Large: $7.50
Extra Topping: $0.60

Target Market(s)

Ages 15-39 including high school students, and young to middle aged workers that feel they need an energy or mood boost.

Industry/Entity Type

Bubble Tea (Non Alcoholic beverage)

Font styles to use
Sans Serif
Script

Colors
0094D4
00A9DD
6FCCEA
C7EBF8
E9F6FB
00AB8E
00BBA5
67D7C9
C6EFE9
E9F9F6
EE7325
F08F49
F5BC92
FAE3D3
FDF4ED
EB3D1F
EC4F4E
F09395
F8D3D4
FCEDEE

Requirements
Must have
• Pictures of bubble tea, Not crowded, easy to read, complimentary colours, prices, pictures must be in round bottom cups and without lid (attached)
Nice to have
• Bubbles or wave pattern
Should not have
• No black background, no fruits, no cartoon looking pictures

```html
<!DOCTYPE html>
<html lang="en">
<head>
<meta charset="UTF-8">
<title>Pearlwave Menu Board</title>
<link href="https://fonts.googleapis.com/css2?family=Caveat+Brush&family=Baloo+2:wght@600&family=Montserrat:wght@400&display=swap" rel="stylesheet">
<style>
  :root {
    --teal: #00bba5;
    --teal-soft: #8ecbc2;
    --salmon: #e99a88;
    --sun: #fde068;
    --coral: #ec6f6a;
    --ink: #1f1f1f;
    --text: #2c2c2c;
    --wash-green: #e4f4dc;
    --wash-yellow: #f8f6d4;
    --paper: #ffffff;
  }
  * { margin: 0; padding: 0; box-sizing: border-box; }
  html, body { width: 1200px; height: 490px; overflow: hidden; background: var(--paper); }
  .menu-board {
    position: relative; width: 1200px; height: 490px; overflow: hidden; isolation: isolate;
    background:
      radial-gradient(ellipse 420px 260px at 560px 40px, var(--wash-green), transparent 70%),
      radial-gradient(ellipse 360px 240px at 1000px 60px, var(--wash-yellow), transparent 70%),
      radial-gradient(ellipse 300px 260px at 80px 420px, var(--wash-yellow), transparent 70%),
      radial-gradient(ellipse 380px 200px at 380px 120px, #eef8e6, transparent 70%),
      var(--paper);
    font-family: "Montserrat", sans-serif;
    color: var(--text);
  }
  .splash { position: absolute; }
  .splash-top-left { left: 0; top: 0; }
  .splash-bottom-right { right: 0; bottom: 0; }

  .art { position: absolute; border-radius: 34px; }
  .art-cup-left { left: 0; top: 170px; width: 68px; height: 138px; border-radius: 0 30px 30px 0;
    background: linear-gradient(180deg, #f6c35a, #f3a94a); }
  .art-cup-milk { left: 352px; top: 168px; width: 64px; height: 142px;
    background: linear-gradient(180deg, #d9d6f2, #c98c5a 60%, #b07a52); }
  .art-cup-berry { left: 708px; top: 168px; width: 84px; height: 138px;
    background: linear-gradient(180deg, #f4b6c2, #e6738d); }
  .art-cup-peach { left: 1114px; top: 200px; width: 62px; height: 116px;
    background: linear-gradient(180deg, #fbd38d, #f5a64a); }
  .art-fruit-lines-top { right: 0; top: 0; width: 140px; height: 150px; border-radius: 0 0 0 60px;
    background: linear-gradient(200deg, rgba(103,215,201,.22), transparent); }
  .art-fruit-lines-bottom { left: 0; bottom: 0; width: 190px; height: 120px; border-radius: 0 60px 0 0;
    background: linear-gradient(20deg, rgba(103,215,201,.22), transparent); }

  .section-title { position: absolute; top: 50px; height: 58px; display: flex; align-items: center; justify-content: center; }
  .section-title svg { position: absolute; inset: 0; width: 100%; height: 100%; }
  .section-title h2 {
    position: relative; font-family: "Caveat Brush", cursive; font-weight: 400;
    font-size: 36px; color: var(--ink); letter-spacing: .5px;
  }
  .title-milk { left: 16px; width: 356px; }
  .title-tea { left: 391px; width: 351px; }
  .title-toppings { left: 766px; width: 357px; }

  .drink-list { position: absolute; list-style: none; }
  .drink-list li {
    position: relative; padding-left: 12px; font-size: 15.5px; line-height: 31px; white-space: nowrap;
  }
  .drink-list li::before {
    content: ""; position: absolute; left: -2px; top: 12px; width: 7px; height: 7px;
    border-radius: 50%; background: var(--coral);
  }
  .list-milk-a { left: 80px; top: 136px; }
  .list-milk-b { left: 244px; top: 136px; }
  .list-tea-a { left: 442px; top: 136px; }
  .list-tea-b { left: 578px; top: 136px; }
  .list-jelly { left: 833px; top: 197px; }
  .list-jelly li { line-height: 29.7px; }
  .list-popping { left: 966px; top: 198px; }
  .list-popping li { line-height: 28.8px; }

  .topping-label { position: absolute; font-family: "Baloo 2", sans-serif; font-weight: 600; color: var(--teal); white-space: nowrap; }
  .label-tapioca { left: 888px; top: 128px; font-size: 18px; }
  .label-jelly { left: 829px; top: 166px; font-size: 17px; }
  .label-popping { left: 963px; top: 166px; font-size: 17px; }

  .price-name { position: absolute; top: 378px; font-family: "Caveat Brush", cursive; font-size: 48px; line-height: 54px; color: var(--teal); white-space: nowrap; }
  .name-regular { left: 356px; }
  .name-large { left: 458px; }
  .name-extra { left: 638px; }
  .price-tag {
    position: absolute; top: 390px; font-family: "Caveat Brush", cursive; font-size: 26px; line-height: 30px;
    color: var(--ink); z-index: 1;
  }
  .price-tag::before {
    content: ""; position: absolute; left: 14px; top: 50%; transform: translateY(-50%);
    width: 44px; height: 44px; border-radius: 50%; background: var(--coral); z-index: -1;
  }
  .tag-regular { left: 379px; }
  .tag-large { left: 558px; }
  .tag-extra { left: 871px; }
</style>
</head>
<body>
<main class="menu-board" aria-label="Pearlwave bubble tea menu">
  <svg class="splash splash-top-left" width="340" height="200" viewBox="0 0 340 200" aria-hidden="true">
    <path d="M0 0 H300 C305 20 290 36 250 40 C215 44 180 46 170 70 C162 90 175 110 150 120 C130 128 118 110 118 90 C118 70 100 60 70 66 C40 72 20 80 0 84 Z" fill="var(--teal)"/>
    <path d="M130 110 C140 140 170 150 190 132 C200 120 182 104 165 110 Z" fill="var(--teal)" opacity=".85"/>
    <circle cx="220" cy="178" r="7" fill="var(--teal-soft)"/>
  </svg>
  <svg class="splash splash-bottom-right" width="150" height="110" viewBox="0 0 150 110" aria-hidden="true">
    <path d="M150 0 V110 H0 C0 70 12 30 50 14 C90 -2 120 2 150 0 Z" fill="var(--teal-soft)"/>
  </svg>

  <div class="art art-fruit-lines-top" role="img" aria-label="Line drawings of fruit"></div>
  <div class="art art-fruit-lines-bottom" role="img" aria-label="Line drawings of fruit"></div>
  <div class="art art-cup-left" role="img" aria-label="Mango bubble tea illustration"></div>
  <div class="art art-cup-milk" role="img" aria-label="Milk tea with pearls illustration"></div>
  <div class="art art-cup-berry" role="img" aria-label="Strawberry bubble tea illustration"></div>
  <div class="art art-cup-peach" role="img" aria-label="Peach bubble tea illustration"></div>

  <div class="section-title title-milk">
    <svg viewBox="0 0 355 54" preserveAspectRatio="none" aria-hidden="true"><path d="M6 6 L350 2 L340 14 L354 26 L342 38 L352 50 L4 52 L14 40 L0 28 L12 16 Z" fill="var(--salmon)"/></svg>
    <h2>Milk Tea</h2>
  </div>
  <div class="section-title title-tea">
    <svg viewBox="0 0 352 54" preserveAspectRatio="none" aria-hidden="true"><path d="M8 4 L348 2 L338 16 L352 28 L340 40 L350 52 L2 50 L14 38 L0 26 L12 14 Z" fill="var(--teal)"/></svg>
    <h2>Green Tea / Red Tea</h2>
  </div>
  <div class="section-title title-toppings">
    <svg viewBox="0 0 350 54" preserveAspectRatio="none" aria-hidden="true"><path d="M6 4 L346 6 L336 18 L350 30 L338 42 L348 52 L4 50 L14 38 L0 26 L12 14 Z" fill="var(--sun)"/></svg>
    <h2>Toppings</h2>
  </div>

  <ul class="drink-list list-milk-a">
    <li>Thai</li><li>Royal</li><li>Original</li><li>Tiger Pearl</li><li>Young Coconut</li><li>Watermelon</li><li>Banana</li>
  </ul>
  <ul class="drink-list list-milk-b">
    <li>Taro</li><li>Lychee</li><li>Honeydew</li><li>Strawberry</li><li>Lavender</li><li>Mango</li><li>Rose</li>
  </ul>
  <ul class="drink-list list-tea-a">
    <li>Peach</li><li>Mango</li><li>Passionfruit</li><li>Watermelon</li><li>Dragonfruit</li>
  </ul>
  <ul class="drink-list list-tea-b">
    <li>Grape</li><li>Lychee</li><li>Strawberry</li><li>Green Apple</li><li>Pomegranate</li>
  </ul>

  <p class="topping-label label-tapioca">Tapioca Pearls</p>
  <p class="topping-label label-jelly">Fruit Jelly</p>
  <p class="topping-label label-popping">Poppings Pearls</p>
  <ul class="drink-list list-jelly">
    <li>Rainbow</li><li>Lychee</li><li>Mango</li><li>Peach</li><li>Grape</li>
  </ul>
  <ul class="drink-list list-popping">
    <li>Peach</li><li>Mango</li><li>Lychee</li><li>Strawberry</li><li>Passionfruit</li><li>Watermelon</li>
  </ul>

  <span class="price-name name-regular" style="left:242px">Regular</span>
  <span class="price-tag tag-regular">$6.50</span>
  <span class="price-name name-large">Large</span>
  <span class="price-tag tag-large">$7.50</span>
  <span class="price-name name-extra">Extra Topping</span>
  <span class="price-tag tag-extra">$0.60</span>
</main>
</body>
</html>
```